Luxury Wine Label for New Startup Winery

We need a wine label for our new winery startup. We have worked with a local designer but do not feel the resulting label / logo have the elevation required to present our brand as a luxury wine. Our winery is called "Harrowgate Vineyards" and we are focused on extremely high quality hand crafted artisan and estate wines from the Pacific Northwest.
We would like to see designs that utilize a tree line, or other imagery that represents the "Harrowgate" part of our company name. Another interesting feature could be wood grain.
A logo will be required based on your design so please design with this in mind:
This logo should be consistent with the wine bottle label design, and should be representative of our high end exclusive wine while giving a sense of place (Oregon/ Pacific Northwest.)
I will supply an image of the design we received from our local designer, PLEASE NOTE: in general we do like wood grain and tree line concepts but feel the execution was poorly done.
ATTN: Logo design should be suitable for use on: Bottles (Red wine/rose/white wine), Bussiness cards, vehicle signage, business signage, etc
P.S.:
If you have a design that is not outside the box we are still interested in seeing it.
Label is for a burgundy style bottle with a label height of 3.5 - 4" and a width of 3.5-4"
any label <= 4"x4" and >=3.5"x3.5" will be acceptable:
HOWEVER Width should be greater than or equal to height due to the bottle format
Target Market(s)
Wine enthusiasts with adequate discretionary budgets to afford $100 bottles of wine.
Industry/Entity Type
Wine / Winery
Requirements
Must have
- A sense of luxury, a feel of exclusivity, and a theme consistent with our product and brand name
Nice to have
- Tree line, wood grain or other wood themes. Serif fonts
Should not have
- anything cheesy, off topic, hard to read script fonts or anything that makes the label hard to read from a few feet away or too busy

```html
<!DOCTYPE html>
<html lang="en">
<head>
<meta charset="utf-8">
<title>Harrowgate Vineyards – Chardonnay Label</title>
<link rel="stylesheet" href="https://fonts.googleapis.com/css2?family=Cormorant+Garamond:ital,wght@0,500;0,600;1,500&display=swap">
<style>
  :root {
    --page: #ffffff;
    --forest: #0d2e28;
    --gold-light: #d9c7a0;
    --gold-mid: #bfa77a;
    --gold-deep: #9c8458;
    --gold-text: #b99b68;
  }
  * { margin: 0; padding: 0; box-sizing: border-box; }
  html, body {
    width: 1200px;
    height: 1000px;
    overflow: hidden;
    background: var(--page);
  }
  .canvas {
    position: relative;
    width: 1200px;
    height: 1000px;
  }
  .label {
    position: absolute;
    left: 236px;
    top: 136px;
    width: 728px;
    height: 728px;
  }
  .label__shape {
    position: absolute;
    inset: 0;
    width: 100%;
    height: 100%;
  }
  .brand {
    position: absolute;
    left: 443px;
    top: 168px;
    transform: translateX(-50%);
    text-align: center;
    color: var(--forest);
    font-family: "Cormorant Garamond", Georgia, serif;
    font-weight: 600;
    white-space: nowrap;
  }
  .brand__name {
    display: block;
    font-size: 46px;
    letter-spacing: 0.04em;
    line-height: 1;
    text-transform: uppercase;
  }
  .brand__sub {
    display: block;
    margin-top: 8px;
    font-size: 28px;
    letter-spacing: 0.06em;
    line-height: 1;
    text-transform: uppercase;
  }
  .varietal {
    position: absolute;
    left: 83px;
    top: 592px;
    color: var(--gold-text);
    font-family: "Cormorant Garamond", Georgia, serif;
    line-height: 1.15;
  }
  .varietal__name {
    display: block;
    font-size: 26px;
    font-weight: 600;
  }
  .varietal__vintage {
    display: block;
    font-size: 26px;
    font-style: italic;
    font-weight: 500;
    letter-spacing: 0.04em;
  }
</style>
</head>
<body>
  <main class="canvas">
    <section class="label" aria-label="Harrowgate Vineyards chardonnay label">
      <svg class="label__shape" viewBox="0 0 485 485" aria-hidden="true">
        <defs>
          <linearGradient id="gold-foil" x1="0" y1="0" x2="1" y2="1">
            <stop offset="0" stop-color="var(--gold-deep)"/>
            <stop offset="0.45" stop-color="var(--gold-light)"/>
            <stop offset="1" stop-color="var(--gold-mid)"/>
          </linearGradient>
          <clipPath id="label-outline">
            <polygon points="0,202 35,165 85,140 90,98 150,80 180,75 270,40 320,2 355,30 395,60 430,90 440,85 485,145 485,485 0,485"/>
          </clipPath>
        </defs>
        <g clip-path="url(#label-outline)">
          <rect class="label__foil" width="485" height="485" fill="url(#gold-foil)"/>
          <path class="label__treeline" role="img" aria-label="Gold-speckled forest tree line illustration"
                d="M0,200 C40,190 60,250 100,240 C140,230 150,200 190,215 C230,230 250,280 290,260 C330,240 360,220 400,230 C440,240 460,220 485,215 L485,485 L0,485 Z"
                fill="var(--forest)"/>
        </g>
      </svg>

      <h1 class="brand">
        <span class="brand__name">Harrowgate</span>
        <span class="brand__sub">Vineyards</span>
      </h1>

      <p class="varietal">
        <span class="varietal__name">chardonnay</span>
        <span class="varietal__vintage">2024</span>
      </p>
    </section>
  </main>
</body>
</html>
```